Tova Brisk Fitness Coaching Project

I am a personal trainer based in London. My services include one-on-one PT sessions, bootcamps.
I would like the design to be minimalistic. With light colours: white, pink, purple.
I specialise in weight loss, flexibility, mobility.

Tova Penrick
Personal Trainer
Email: tova.penrick@mailgrove.net
tel: 07500 918 243
Instagram: Tova Brisk

Target Market(s)

adults, mostly females (age 18-50).

Industry/Entity Type

Fitness

Contact Information for Business Card

Tova Penrick
Personal Trainer
tel: 07500 918 243
Instagram: Tova Brisk

Font styles to use
Serif

Colors
eea4c8
fbd4d5
fdf9cf
cfeae6
cee9f5

Requirements
Nice to have
• minimalistic style
• easy to read and remember

```html
<!DOCTYPE html>
<html lang="en">
<head>
<meta charset="utf-8">
<title>Tova Brisk Fitness Coaching – Business Card</title>
<link href="https://fonts.googleapis.com/css2?family=Saira+Condensed:wght@700&family=Open+Sans:wght@400&display=swap" rel="stylesheet">
<style>
  :root {
    --page-bg: #f1ede8;
    --card-white: #ffffff;
    --pink-strong: #eda3c9;
    --pink-soft: #fbd4d5;
    --cream: #fdf9cf;
    --logo-grey: #e6e6e6;
    --ink: #111111;
    --ink-soft: #555555;
    --on-pink: #ffffff;
  }
  * { margin: 0; padding: 0; box-sizing: border-box; }
  html, body { width: 1200px; height: 1000px; overflow: hidden; }
  body { background: var(--page-bg); position: relative; font-family: "Open Sans", sans-serif; }

  .card {
    position: absolute; left: 280px; width: 640px; height: 366px;
    overflow: hidden; box-shadow: 0 6px 18px rgba(0,0,0,0.12);
  }
  .card--back { top: 90px; background: var(--cream); }
  .card--front { top: 544px; background: var(--card-white); }

  /* back */
  .back-lower { position: absolute; left: 0; right: 0; top: 154px; bottom: 0; background: var(--pink-soft); }
  .brand-mark { position: absolute; display: flex; align-items: center; gap: 10px; }
  .brand-mark__square { width: 64px; height: 64px; background: var(--logo-grey); }
  .brand-mark__name { font-family: "Saira Condensed", sans-serif; font-weight: 700; font-size: 24px; color: var(--ink); letter-spacing: 1px; text-transform: uppercase; }
  .card--back .brand-mark { left: 250px; top: 122px; }
  .back-email { position: absolute; left: 128px; top: 270px; font-size: 12px; letter-spacing: 3px; color: var(--ink-soft); }

  /* front */
  .contact-panel { position: absolute; top: 0; right: 0; bottom: 0; width: 295px; background: var(--pink-strong); padding: 72px 0 0 36px; }
  .card--front .brand-mark { left: 30px; top: 42px; }
  .card--front .brand-mark__square { width: 58px; height: 58px; }
  .card--front .brand-mark__name { font-size: 20px; }
  .trainer { position: absolute; left: 62px; top: 196px; text-align: right; }
  .trainer__name { font-family: "Saira Condensed", sans-serif; font-weight: 700; font-size: 50px; line-height: 1; color: var(--ink); }
  .trainer__role { font-size: 15px; color: var(--ink); margin-top: 2px; }
  .contact-row { display: flex; align-items: center; gap: 14px; height: 34px; margin-bottom: 26px; color: var(--on-pink); font-size: 14px; }
  .contact-row svg { width: 18px; height: 18px; flex: none; }
</style>
</head>
<body>
  <section class="card card--back" aria-label="Card back">
    <div class="back-lower"></div>
    <div class="brand-mark">
      <span class="brand-mark__square"></span>
      <span class="brand-mark__name">Tova Brisk</span>
    </div>
    <p class="back-email">tova.penrick@mailgrove.net</p>
  </section>

  <section class="card card--front" aria-label="Card front">
    <div class="brand-mark">
      <span class="brand-mark__square"></span>
      <span class="brand-mark__name">Tova Brisk</span>
    </div>
    <div class="trainer">
      <h1 class="trainer__name">Tova Penrick</h1>
      <p class="trainer__role">Personal Trainer</p>
    </div>
    <div class="contact-panel">
      <div class="contact-row">
        <svg viewBox="0 0 24 24" aria-hidden="true"><path fill="#fff" d="M6.6 10.8a15.1 15.1 0 0 0 6.6 6.6l2.2-2.2c.3-.3.7-.4 1-.2 1.1.4 2.3.6 3.6.6.6 0 1 .4 1 1V20c0 .6-.4 1-1 1A17 17 0 0 1 3 4c0-.6.4-1 1-1h3.5c.6 0 1 .4 1 1 0 1.3.2 2.5.6 3.6.1.3 0 .7-.2 1z"/></svg>
        <span>07500 918 243</span>
      </div>
      <div class="contact-row">
        <svg viewBox="0 0 24 24" aria-hidden="true"><circle cx="12" cy="12" r="9" fill="#fff"/></svg>
        <span>www.Snapreel/ Tova Brisk</span>
      </div>
      <div class="contact-row">
        <svg viewBox="0 0 24 24" aria-hidden="true"><rect x="3" y="5" width="18" height="14" fill="none" stroke="#fff" stroke-width="2"/><path d="M3 6l9 7 9-7" fill="none" stroke="#fff" stroke-width="2"/></svg>
        <span>tova.penrick@mailgrove.net</span>
      </div>
    </div>
  </section>
</body>
</html>
```